Classy, Elegant, Simple Business Card Design

Looking to have a classy, simple, and elegant design. Want a top notch designed business card. I really like the look of the new brivo credit card. I also like the design I attached. I am trying to reach 21-29 year old females for booking us for there wedding or event. We offer Disc Jockey Service, Photo Booth Rentals, and Uplighting .

Target Market(s)

21-28 year old females

Contact Information for Business Card

Has to have logo, website, email, and phone number

Font styles to use
Other font styles liked:
• open to font choice, modern, clean
Designer to choose
33a6d7
0791cd
0555a3
ffffff

Requirements
Must have
• Has to have logo, website, email, and phone number
Nice to have
• I really like the design of the new brivo credit card. I also included my logo and some designs I like
Should not have
• clutter or too much info

```html
<!DOCTYPE html>
<html lang="en">
<head>
<meta charset="utf-8">
<title>Lumenbay Event Group — Business Card</title>
<link rel="stylesheet" href="https://fonts.googleapis.com/css2?family=Jost:wght@400;500&display=swap">
<style>
  :root {
    --page: #ffffff;
    --card-edge: #111111;
    --ink: #111111;
    --label: #00bde8;
    --brand-deep: #0555a3;
    --brand-mid: #0791cd;
    --brand-light: #33a6d7;
    --sheen-light: #fbfcfc;
    --sheen-mid: #f1f3f3;
    --sheen-dark: #e4e9e9;
  }
  html, body {
    margin: 0;
    padding: 0;
    width: 1200px;
    height: 724px;
    overflow: hidden;
    background: var(--page);
  }
  .canvas {
    position: relative;
    width: 1200px;
    height: 724px;
  }
  .card {
    position: absolute;
    left: 56px;
    top: 59px;
    width: 1088px;
    height: 605px;
    box-sizing: border-box;
    border: 1px solid var(--card-edge);
    overflow: hidden;
    font-family: "Jost", "Futura", sans-serif;
    background:
      linear-gradient(135deg, transparent 0 62%, rgba(255,255,255,0.8) 70%, transparent 80%),
      linear-gradient(45deg,
        var(--sheen-mid) 0%,
        var(--sheen-light) 14%,
        var(--sheen-mid) 22%,
        var(--sheen-dark) 30%,
        var(--sheen-light) 40%,
        var(--sheen-mid) 48%,
        var(--sheen-dark) 54%,
        var(--sheen-light) 62%,
        var(--sheen-mid) 70%,
        var(--sheen-light) 78%,
        var(--sheen-dark) 84%,
        var(--sheen-light) 92%,
        var(--sheen-mid) 100%);
  }
  .brand {
    position: absolute;
    left: 60px;
    top: 70px;
    width: 280px;
    text-align: center;
    color: var(--brand-mid);
    font-weight: 500;
  }
  .brand-dot {
    display: block;
    width: 78px;
    height: 78px;
    margin: 0 auto 26px;
    border-radius: 50%;
    background: var(--brand-mid);
  }
  .brand-name {
    display: block;
    font-size: 40px;
    line-height: 1;
    letter-spacing: 1px;
  }
  .brand-sub {
    display: block;
    margin-top: 8px;
    font-size: 15px;
    letter-spacing: 9px;
  }
  .contact {
    position: absolute;
    left: 428px;
    top: 440px;
    margin: 0;
    padding: 0;
    list-style: none;
  }
  .contact-row {
    display: flex;
    align-items: baseline;
    height: 44px;
    color: var(--ink);
  }
  .contact-label {
    width: 54px;
    color: var(--label);
    font-size: 30px;
    font-weight: 400;
    text-align: center;
  }
  .contact-value {
    font-size: 33px;
    font-weight: 500;
    letter-spacing: 0.6px;
  }
  .contact-phone .contact-value { letter-spacing: 2px; }
</style>
</head>
<body>
  <div class="canvas">
    <section class="card">
      <div class="brand">
        <span class="brand-dot" aria-hidden="true"></span>
        <span class="brand-name">LUMENBAY</span>
        <span class="brand-sub">EVENT GROUP</span>
      </div>
      <ul class="contact">
        <li class="contact-row contact-phone"><span class="contact-label">T</span><span class="contact-value">+1555-014-2297</span></li>
        <li class="contact-row contact-email"><span class="contact-label">E</span><span class="contact-value">hello@lumenbayeventgroup.com</span></li>
        <li class="contact-row contact-web"><span class="contact-label">W</span><span class="contact-value">www.lumenbayeventgroup.com</span></li>
      </ul>
    </section>
  </div>
</body>
</html>
```